Personal loan pre-approval

We are a credit union sending out pre-approvals for personal loans. I am attaching a letter that we sent out during previous pre-approvals. The fine print needs to be included on the postcard from the letter, but the rest is just a guide. The theme I'm thinking of may be Easy, Cold Hard Cash, but I'm not stuck on it. Thanks.

http://www.brightquarry.net/gallerydetail.aspx?sectionID=143&photoID=104

The cash banner is an example of what I had in mind.

We don't want the actual letter on the postcard, it was meant to be a guide only as to what we are selling. The front page should be explaining that they are pre-approved for a personal loan, say up $10,000, at a rate of 7.99% APR*. It should be mentioned how they are pre-approved, which means no credit check, no proof of income needed. Somewhere, either on the front or the back, needs to be the fine print in a discreet fashion. look at the link I provide for some guidance. Thanks!
Updates

Industry/Entity Type

Union

Requirements
Must have
• Must have fine print on postcard that is on example letter.
Should not have
• Should not have the entire letter on the postcard

```html
<!DOCTYPE html>
<html lang="en">
<head>
<meta charset="utf-8">
<title>Signature Loan Pre-Approval Postcard</title>
<link rel="stylesheet" href="https://fonts.googleapis.com/css2?family=Oswald:wght@500;700&display=swap">
<style>
  :root {
    --blue-deep: #0b3ea6;
    --blue-mid: #1f5fd2;
    --blue-light: #5c8fe6;
    --wash: #eef2fb;
    --money-light: #d9ddd2;
    --money-mid: #a7b39b;
    --money-dark: #6f7f66;
    --lime: #c3df3a;
    --term-green: #93c21f;
    --white: #ffffff;
  }
  html, body {
    margin: 0;
    padding: 0;
    width: 1200px;
    height: 809px;
    overflow: hidden;
    background: var(--white);
  }
  .postcard {
    position: relative;
    width: 1200px;
    height: 809px;
    overflow: hidden;
    font-family: "Oswald", "Arial Narrow", sans-serif;
    color: var(--white);
    background: linear-gradient(90deg, var(--wash) 0%, var(--wash) 30%, var(--blue-light) 46%, var(--blue-mid) 62%, var(--blue-deep) 100%);
  }
  .cash-photo {
    position: absolute;
    left: 0;
    top: 0;
    width: 560px;
    height: 809px;
    background:
      radial-gradient(ellipse at 30% 25%, var(--money-mid) 0%, transparent 55%),
      radial-gradient(ellipse at 20% 75%, var(--money-dark) 0%, transparent 50%),
      linear-gradient(90deg, var(--money-light) 0%, var(--money-mid) 45%, rgba(167,179,155,0) 100%);
    opacity: 0.9;
  }
  .headline {
    position: absolute;
    left: 512px;
    top: 40px;
    margin: 0;
    font-weight: 700;
    font-size: 74px;
    line-height: 1.02;
    letter-spacing: 0.5px;
    text-transform: uppercase;
  }
  .headline .accent { color: var(--lime); }
  .offer {
    position: absolute;
    left: 512px;
    top: 222px;
    text-transform: uppercase;
    font-weight: 700;
  }
  .offer-amount {
    margin: 0;
    font-size: 74px;
    line-height: 1;
    color: var(--lime);
  }
  .offer-label {
    margin: 4px 0 0;
    font-size: 52px;
    line-height: 1.02;
  }
  .offer-note {
    margin: 4px 0 0;
    font-size: 12px;
    font-weight: 500;
    letter-spacing: 0.3px;
  }
  .offer-rate {
    margin: 28px 0 0;
    font-size: 50px;
    line-height: 1;
    color: var(--lime);
  }
  .term-box {
    position: absolute;
    left: 804px;
    top: 300px;
    width: 322px;
    height: 167px;
    border-radius: 10px;
    background: var(--white);
    display: flex;
    align-items: center;
    justify-content: center;
    text-align: center;
    font-weight: 700;
    font-size: 50px;
    line-height: 1.05;
    color: var(--term-green);
    text-transform: uppercase;
  }
  .brand {
    position: absolute;
    left: 832px;
    top: 492px;
    width: 280px;
    display: flex;
    align-items: center;
    gap: 14px;
  }
  .brand-mark {
    width: 40px;
    height: 40px;
    background: var(--white);
    flex: none;
  }
  .brand-name {
    font-weight: 700;
    font-size: 26px;
    line-height: 1.05;
    text-transform: uppercase;
    color: var(--white);
  }
</style>
</head>
<body>
<main class="postcard">
  <div class="cash-photo" role="img" aria-label="Photo of scattered hundred-dollar bills"></div>

  <h1 class="headline">You have been<br><span class="accent">Pre-approved</span> for:</h1>

  <section class="offer">
    <p class="offer-amount">$7,000</p>
    <p class="offer-label">Signature<br>Loan,</p>
    <p class="offer-note">Including existing loan balances*</p>
    <p class="offer-rate">9.95%</p>
    <p class="offer-label">Annual<br>Percentage Rate</p>
  </section>

  <div class="term-box">Up to 60<br>Month Term</div>

  <div class="brand">
    <span class="brand-mark"></span>
    <span class="brand-name">Harbor Valley Teachers<br>Credit Union</span>
  </div>
</main>
</body>
</html>
```